UPDATE 2: I HAVE ATTACHED TWO PHOTOS; PLEASE CONSIDER USING EITHER ONE IN A NEW DESIGN. THANK YOU.
UPDATE: I HAVE INCLUDED 4 SAMPLE BOOK COVERS THAT I LIKE TO HELP YOU ORIENT YOUR DESIGN WORK
Looking for book cover, spine, and back for a MEMOIR. Details:
TITLE: Mama's Quiet Orchard
AUTHOR: Lorivel Brashton
GENRE: Memoir
STYLE REQUESTED: Abstract and colorful; designers are welcome to get creative. Note that the memoir takes place largely in a poor African American city.
BOOK SUMMARY: As a young girl, Lorivel Brashton—or “Rivvy” to her friends and family—discovers the man she thought was her father wasn’t, and her real biological father wants little if anything to do with her. What follows is the story of a girl’s longing, a longing disturbed by abuse, disappointment, and loneliness.
Set against the backdrop of Gary, Indiana—the then “murder capital of the world”—Mama’s Quiet Orchard follows Lorivel as she searches and grows, following a path that eventually leads her to self-discovery and self-confidence.
Template provided for InDesign. Please note margins and bleed areas. Make sure any letters/words are at least one inch from edges. On spine, leave three inches at bottom for publisher's logo.
Updates
To all designers: Please note that there should NOT be any images of people as part of your designs. Thank you, and my apologies for not mentioning that in the initial ask.

```html
<!DOCTYPE html>
<html lang="en">
<head>
<meta charset="utf-8">
<title>Mama's Quiet Orchard — Memoir Cover</title>
<link rel="stylesheet" href="https://fonts.googleapis.com/css2?family=Barlow+Semi+Condensed:wght@300;700&family=Spectral:wght@400&display=swap">
<style>
  :root {
    --page-bg: #e4e4e4;
    --title-ink: #0c1420;
    --light-ink: #ffffff;
    --sky-top: #7f8fd2;
    --sky-pink: #c9a0bf;
    --sky-glow: #f4b866;
    --horizon: #3f4a45;
    --water: #9cc6c8;
    --water-warm: #e0b87a;
    --deck-mid: #8c4f33;
    --deck-dark: #5e3422;
  }
  * { margin: 0; padding: 0; box-sizing: border-box; }
  html, body {
    width: 1200px;
    height: 800px;
    overflow: hidden;
    background: var(--page-bg);
  }
  .canvas {
    width: 1200px;
    height: 800px;
    display: flex;
    align-items: center;
    justify-content: center;
  }
  .book-cover {
    position: relative;
    width: 472px;
    height: 720px;
    overflow: hidden;
  }
  .cover-photo {
    position: absolute;
    inset: 0;
    background:
      radial-gradient(ellipse 60% 18% at 92% 37%, rgba(255, 196, 90, 0.9), rgba(255, 196, 90, 0) 70%),
      radial-gradient(ellipse 30% 30% at 88% 58%, rgba(224, 184, 122, 0.7), rgba(224, 184, 122, 0) 70%),
      radial-gradient(ellipse 70% 45% at 55% 88%, var(--deck-mid), rgba(140, 79, 51, 0) 75%),
      linear-gradient(180deg,
        var(--sky-top) 0%,
        var(--sky-pink) 18%,
        #a9b3d8 30%,
        var(--sky-glow) 37%,
        var(--horizon) 39.5%,
        var(--horizon) 41%,
        var(--water) 45%,
        #86b5b8 62%,
        var(--deck-mid) 78%,
        var(--deck-dark) 100%);
  }
  .cover-title {
    position: absolute;
    top: 40px;
    left: 0;
    right: 0;
    text-align: center;
    font-family: "Barlow Semi Condensed", sans-serif;
    font-weight: 700;
    font-size: 80px;
    line-height: 74px;
    text-transform: uppercase;
    color: var(--title-ink);
    letter-spacing: 1px;
  }
  .cover-genre {
    position: absolute;
    top: 262px;
    left: 0;
    right: 0;
    text-align: center;
    font-family: "Barlow Semi Condensed", sans-serif;
    font-weight: 300;
    font-size: 28px;
    letter-spacing: 7px;
    text-transform: uppercase;
    color: var(--light-ink);
  }
  .cover-author {
    position: absolute;
    bottom: 30px;
    left: 0;
    right: 0;
    text-align: center;
    font-family: "Spectral", serif;
    font-weight: 400;
    font-size: 36px;
    letter-spacing: 3px;
    color: var(--light-ink);
  }
</style>
</head>
<body>
  <main class="canvas">
    <article class="book-cover">
      <div class="cover-photo" role="img" aria-label="Photograph of a long wooden pier stretching across a calm lake toward a pink and orange sunset over a misty treeline"></div>
      <h1 class="cover-title">Mama’s<br>Quiet<br>Orchard</h1>
      <p class="cover-genre">Memoir</p>
      <p class="cover-author">Lorivel Brashton</p>
    </article>
  </main>
</body>
</html>
```